Business cards for education company

We need a business card design for a relatively new company based in Queensland and operating across Australia. We resell diploma level education courses which include Business, Management, Finance, Community Services & Government courses. We offer over 20 different courses.
The target market is for anyone 16 years of age and older. There is no age limit.

We would like to see the design use the color blue and silver. The final design should communicate professionalism and a bright future.

We sell education but are also promoting the career they see themselves in 2-3 years in the future

Our company logo is attached.

Target Market(s)

We target all age groups above 16 years of age. The main target market would be people aged between 17-35.

We focus on those people who cannot make it into University or do not want to commit the time to a full degree.

Industry/Entity Type

Education

Requirements
Must have
• Professional
Company logo
website
Contact details:

Please use the following example:

Lionel Parfitt
Senior Education Consultant
0417 386 591
Lionel.parfitt@brightwaylearninghub.com.au
www.brightwaylearninghub.com.au

```html
<!DOCTYPE html>
<html lang="en">
<head>
<meta charset="utf-8">
<title>Brightway Learning Hub – Business Cards</title>
<link rel="stylesheet" href="https://fonts.googleapis.com/css2?family=Exo+2:wght@400;600&display=swap">
<style>
  :root {
    --bg: #e4e6ea;
    --card-white: #ffffff;
    --card-silver: #e9ecf0;
    --blue-light: #2a8ee0;
    --blue-mid: #1467c0;
    --blue-dark: #0b3f8c;
    --navy: #123a78;
    --edge-black: #101216;
    --text-white: #ffffff;
  }
  * { box-sizing: border-box; margin: 0; padding: 0; }
  html, body { width: 1200px; height: 881px; overflow: hidden; }
  body {
    background: var(--bg);
    font-family: "Exo 2", "Trebuchet MS", sans-serif;
    position: relative;
  }
  .card {
    position: absolute;
    width: 600px;
    height: 343px;
    background: linear-gradient(135deg, var(--card-white) 40%, var(--card-silver));
    overflow: hidden;
    box-shadow: 0 10px 28px rgba(0,0,0,0.22);
  }
  .card--back { left: 120px; top: 70px; }
  .card--front { left: 480px; top: 470px; }

  .brand {
    position: absolute;
    display: flex;
    align-items: center;
    gap: 12px;
  }
  .brand__dot {
    width: 46px; height: 46px;
    border-radius: 50%;
    background: var(--blue-mid);
    flex: none;
  }
  .brand__name {
    color: var(--navy);
    font-weight: 600;
    font-size: 24px;
    line-height: 1.05;
    letter-spacing: 0.5px;
  }
  .card--back .brand { left: 150px; top: 128px; }
  .card--front .brand { left: 330px; top: 140px; }
  .card--front .brand__name { font-size: 22px; }

  .web-band {
    position: absolute;
    right: 0; top: 258px;
    width: 210px; height: 26px;
    background: linear-gradient(90deg, var(--blue-light), var(--blue-dark));
    clip-path: polygon(6% 0, 100% 0, 100% 100%, 0 100%);
    color: var(--text-white);
    font-size: 10px;
    display: flex; align-items: center;
    padding-left: 24px;
  }

  .front-panel { position: absolute; inset: 0; }
  .contact {
    position: absolute;
    left: 28px; top: 24px;
    color: var(--text-white);
  }
  .contact__name { font-size: 17px; font-weight: 600; letter-spacing: 1px; text-transform: uppercase; }
  .contact__title { font-size: 12px; margin-top: 2px; }
  .contact__address { font-size: 12px; line-height: 1.45; margin-top: 34px; }
  .contact__list { list-style: none; margin-top: 26px; }
  .contact__list li {
    display: flex; align-items: center; gap: 8px;
    font-size: 9.5px; height: 19px;
  }
  .contact__list svg { width: 12px; height: 12px; flex: none; }
</style>
</head>
<body>

<section class="card card--back">
  <div class="brand">
    <span class="brand__dot"></span>
    <span class="brand__name">BRIGHTWAY<br>LEARNING HUB</span>
  </div>
  <div class="web-band">www.brightwaylearninghub.com.au</div>
</section>

<section class="card card--front">
  <svg class="front-panel" viewBox="0 0 600 343" width="600" height="343">
    <defs>
      <radialGradient id="panelBlue" cx="0.45" cy="0.35" r="0.75">
        <stop offset="0" stop-color="#2a8ee0"/>
        <stop offset="0.6" stop-color="#1467c0"/>
        <stop offset="1" stop-color="#0b3f8c"/>
      </radialGradient>
    </defs>
    <path d="M0 0 H414 C344 70 298 210 304 343 H0 Z" fill="var(--edge-black)"/>
    <path d="M0 0 H400 C330 70 284 210 290 343 H0 Z" fill="url(#panelBlue)"/>
  </svg>

  <div class="contact">
    <p class="contact__name">Lionel Parfitt</p>
    <p class="contact__title">Managing Director</p>
    <p class="contact__address">Level 4, 120 Eagle St<br>Brisbane QLD</p>
    <ul class="contact__list">
      <li>
        <svg viewBox="0 0 12 12"><path d="M3 1 L5 3.5 L4 5 Q5 7 7 8 L8.5 7 L11 9 L9.5 11 Q4 10 1 3 Z" fill="#fff"/></svg>
        0417 386 591
      </li>
      <li>
        <svg viewBox="0 0 12 12"><rect x="3" y="0.5" width="6" height="11" rx="1" fill="#fff"/><rect x="4" y="2" width="4" height="7" fill="#1467c0"/></svg>
        0417 386 591
      </li>
      <li>
        <svg viewBox="0 0 12 12"><rect x="1" y="5" width="10" height="6" rx="1" fill="#fff"/><rect x="3" y="1" width="6" height="4" fill="#fff"/></svg>
        0417 386 591
      </li>
      <li>
        <svg viewBox="0 0 12 12"><rect x="0.5" y="2" width="11" height="8" fill="#fff"/><path d="M0.5 2 L6 7 L11.5 2" stroke="#1467c0" fill="none"/></svg>
        Lionel.parfitt@brightwaylearninghub.com.au
      </li>
      <li>
        <svg viewBox="0 0 12 12"><circle cx="6" cy="6" r="5" stroke="#fff" fill="none"/><ellipse cx="6" cy="6" rx="2.2" ry="5" stroke="#fff" fill="none"/><path d="M1 6 H11" stroke="#fff"/></svg>
        www.brightwaylearninghub.com.au
      </li>
    </ul>
  </div>

  <div class="brand">
    <span class="brand__dot"></span>
    <span class="brand__name">BRIGHTWAY<br>LEARNING HUB</span>
  </div>
</section>

</body>
</html>
```